Neue Website fuer Software-Firma (CMS: Joomla, Responsive Design)
Zielgruppe
Die VANTRIX ist ein Software- und Beratungshaus im Lager- und Produktionslogistikbereich. Unsere Kunden sind Industriefirmen und Logistikdienstleister, die ein oder mehrere Laeger bewirtschaften und dafuer eine Software und mobile Datenerfassung einsetzen. Fast alle unserer Kunden haben KVT im Einsatz.
Aufgabenstellung
Unsere aktuelle Website wurde seit langem nicht mehr gepflegt und ist veraltet.
Wir moechten die neue Website gern mit dem CMS Joomla betreiben (ggf. waere auch Wordpress moeglich). Gern koennen Sie als Basis ein bereits existierendes (freies) Theme verwenden, wenn es entweder bereits alle Ansprueche erfuellt oder Sie es entsprechend anpassen.
Die neue Website soll in jedem Fall responsive sein, d.h. sowohl auf Desktop, Tablet und Smartphone funktionieren und das Design entsprechend anpassen.
Unsere aktuelle Seite steht unter www.vantrix-lagerwerk.example
Eine Seite, die uns besonders gut gefaellt, ist www.quendal.example (die sich auch teilweise an die gleichen Kunden richtet).
Wir moechten ein klares Design. Ein Beispiel, wie eines unserer Dashboards unserer Software aussieht, finden Sie anbei. Die Farbgestaltung darin wird jedoch noch geaendert. Sie wird eher in Richtung der Farbgestaltung der Quendal-Website gehen, jedoch immer noch grundsaetzlich hell sein. Evtl. koennen Sie Elemente daraus aufgreifen? Es soll in jedem Fall ersichtlich sein, dass Website und Software von der gleichen Firma sind.
Es soll moeglichst viel mit Grafiken gearbeitet werden – aehnlich der Quendal-Seite unter der Dia-Show. Diese muessen aber nicht zwingend farbig sein. Ein Mockup fuer einfarbige Grafiken unterhalb einer Diashow habe ich hier erstellt: https://helgard07.seitenbau.example/meinewebsite-1 Bitte orientieren Sie sich aber nicht an dieser Seite selbst – das war nur ein Probierbeispiel.
Desweiteren soll die Seite suchmaschinenfreundlich sein.
In Ihren Leistungen enthalten sein soll:
- Erstellung der Homepage incl.
o Menu (wie bei Quendal soll es ausklappbar sein und mind. 2 Ebenen koennen)
o Login-Button der einen externen Link aufruft
o Auswahl der Sprache (und damit Verlinkung zu jeweils der Homepage in der
ausgewaehlten Sprache
o Moeglichkeit zum Chat
o Suchfeld zum Durchsuchen aller S..

```html
<!DOCTYPE html>
<html lang="en">
<head>
<meta charset="utf-8">
<title>VANTRIX – Software Solutions for Logistics</title>
<link href="https://fonts.googleapis.com/css2?family=Lato:wght@300;400;700&display=swap" rel="stylesheet">
<style>
:root{
  --navy:#1b2a5a;
  --ink:#333a44;
  --muted:#6b7380;
  --red:#d0021b;
  --topbar:#5c6a79;
  --band:#1a2331;
  --light:#f6f6f6;
  --news-bg:#ececec;
  --map:#e8eaed;
  --blue:#2b6fd6;
  --green:#2ea336;
  --orange:#ff8a00;
  --pink:#d81b4f;
  --link:#2456b8;
}
*{margin:0;padding:0;box-sizing:border-box}
html,body{width:781px;height:1200px;overflow:hidden}
body{font-family:"Lato",sans-serif;color:var(--ink);background:#fff;position:relative;font-size:6px}
.abs{position:absolute}
/* top bar */
.topbar{left:0;top:0;width:781px;height:20px;background:var(--topbar);color:#fff;font-size:6px}
.topbar span{position:absolute;top:6px}
/* header */
.header{left:0;top:20px;width:781px;height:37px;background:#fff;border-bottom:1px solid #e3e3e3}
.brand{left:158px;top:9px;font-weight:700;font-size:17px;color:#1a3d9c;letter-spacing:.5px}
.brand-sub{left:158px;top:28px;font-size:4.5px;color:var(--muted)}
.menu-toggle{left:237px;top:0;width:60px;height:37px;border-left:1px solid #eee;border-right:1px solid #eee}
.menu-toggle .bars{position:absolute;left:10px;top:13px;width:16px}
.menu-toggle .bars i{display:block;height:2px;background:var(--red);margin-bottom:3px}
.menu-toggle b{position:absolute;left:33px;top:14px;font-weight:400;font-size:8px;color:var(--red)}
.search{left:515px;top:10px;width:107px;height:19px;border:1px solid #ddd;font-size:6px;font-style:italic;color:#aaa;padding:5px 6px}
.search svg{position:absolute;right:6px;top:4px}
/* hero */
.hero{left:0;top:57px;width:781px;height:253px;background:linear-gradient(100deg,#6f7c8c 0%,#b4aa94 30%,#8e97a6 55%,#5b6e8d 75%,#d9dde3 100%)}
.hero-title{left:180px;top:143px;font-size:22px;line-height:24px;color:#fff;font-weight:400}
.cta{left:183px;top:208px;width:106px;height:21px;background:var(--red);color:#fff;font-size:10px;text-align:center;line-height:21px}
.dots{left:372px;top:294px}
.dots i{display:inline-block;width:6px;height:6px;border-radius:50%;border:1px solid #fff;margin-right:4px}
.dots i.on{background:var(--red);border-color:var(--red)}
.dropdown{left:237px;top:57px;width:160px;height:85px;font-size:6.5px}
.dropdown .lvl1{position:absolute;left:0;top:0;width:68px;height:85px;background:#eef0f3;padding:6px 6px;line-height:12px}
.dropdown .lvl2{position:absolute;left:68px;top:0;width:92px;height:85px;background:#dde1e6;padding:9px 7px;line-height:12px}
.dropdown .active{color:var(--red)}
/* experts band */
.experts{left:0;top:310px;width:781px;height:52px;background:var(--band)}
.experts .lead{position:absolute;left:0;top:0;width:231px;height:52px;background:var(--red);color:#fff;font-weight:300;font-size:12px;line-height:15px;padding:12px 0 0 160px}
.expert{position:absolute;top:14px;width:90px;text-align:center;color:#fff;font-size:6.5px}
.expert svg{display:block;margin:0 auto 4px}
.chat{left:745px;top:322px;width:36px;height:37px;background:var(--red)}
/* services */
.services{left:0;top:362px;width:781px;height:302px;background:var(--light)}
.h2{position:absolute;width:781px;text-align:center;color:var(--navy);font-weight:400}
.intro{left:158px;top:408px;width:464px;text-align:center;font-size:6px;line-height:8px;color:var(--muted);font-weight:300}
.card{position:absolute;top:442px;width:107px;height:190px;background:#fff}
.card .photo{height:114px}
.card .label{height:18px;color:#fff;font-size:8px;padding:4px 5px}
.card p{font-size:6px;line-height:8px;color:var(--muted);padding:9px 8px;font-weight:300}
/* industries */
.industry{position:absolute;top:730px;width:92px;text-align:center;font-size:6.5px;line-height:8px;color:var(--navy)}
.industry svg{display:block;margin:0 auto 6px}
/* news */
.news{left:0;top:786px;width:781px;height:199px;background:var(--news-bg)}
.news-item{position:absolute;top:858px;width:107px}
.news-item .photo{height:61px}
.news-item h3{font-weight:400;font-size:7.5px;line-height:9px;color:var(--link);padding:5px 1px}
/* clients */
.clients{left:0;top:985px;width:781px;height:43px;background:#fff}
.client{position:absolute;top:1002px;font-size:9px;color:#b9bdc3;font-weight:400;letter-spacing:.5px}
/* maps */
.map{top:1028px;height:145px;background:linear-gradient(135deg,#eceef0,#e2e5e8)}
.tag{position:absolute;background:#1b2433;color:#fff;font-size:6.5px;padding:2px 4px}
.addr{position:absolute;font-size:6px;line-height:7.8px;color:var(--ink);font-weight:300}
.addr a{color:var(--red);text-decoration:none}
/* footer */
.footer{left:0;top:1173px;width:781px;height:27px;background:#fff;border-top:1px solid #e3e3e3;font-size:6px;color:var(--muted);font-weight:300}
</style>
</head>
<body>

<div class="abs topbar">
  <span style="left:158px">&#9675; Support</span>
  <span style="left:218px">&#9993; info@vantrix-lagerwerk.example</span>
  <span style="left:430px">My Account</span>
  <span style="left:490px">Call</span>
  <span style="left:530px">English</span>
</div>

<header class="abs header">
  <div class="abs brand">VANTRIX</div>
  <div class="abs brand-sub">Software Solutions For Logistics</div>
  <div class="abs menu-toggle"><div class="bars"><i></i><i></i><i></i></div><b>Menu</b></div>
  <div class="abs search">Enter keyword
    <svg width="9" height="9" viewBox="0 0 10 10"><circle cx="4" cy="4" r="3" fill="none" stroke="#d0021b" stroke-width="1"/><line x1="6.2" y1="6.2" x2="9" y2="9" stroke="#d0021b" stroke-width="1"/></svg>
  </div>
</header>

<section class="abs hero" role="img" aria-label="Photo: warehouse worker scanning stock between high shelves"></section>
<h1 class="abs hero-title">We are conectiong dots in<br>your logistic business</h1>
<div class="abs cta">CONTACT US</div>
<div class="abs dots"><i class="on"></i><i></i><i></i><i></i></div>

<nav class="abs dropdown">
  <div class="lvl1">About us<br><span class="active">Services</span><br>Clients<br>News<br>Contact</div>
  <div class="lvl2">KVT Development<br>Warehouse Managemen<br><span class="active">Automation / Integration</span><br>Development<br>Maintance</div>
</nav>

<section class="abs experts">
  <div class="lead">We are<br>Experts in:</div>
  <div class="expert" style="left:254px">
    <svg width="16" height="16" viewBox="0 0 16 16"><path d="M2 15V8l4 2V8l4 2V3h2v12z" fill="#2b6fd6"/></svg>PRODUCTION</div>
  <div class="expert" style="left:346px">
    <svg width="16" height="16" viewBox="0 0 16 16" fill="none" stroke="#2ea336"><rect x="5" y="1" width="6" height="6"/><rect x="1" y="9" width="6" height="6"/><rect x="9" y="9" width="6" height="6"/></svg>WAREHOUSING</div>
  <div class="expert" style="left:438px">
    <svg width="20" height="16" viewBox="0 0 20 16"><path d="M5 13a4 4 0 0 1 0-8 5 5 0 0 1 9-1 4.5 4.5 0 0 1 1 9z" fill="none" stroke="#ff8a00"/><rect x="8" y="7" width="5" height="5" fill="#ff8a00"/></svg>KVT</div>
  <div class="expert" style="left:530px">
    <svg width="22" height="16" viewBox="0 0 22 16" fill="none" stroke="#d81b4f"><rect x="1" y="4" width="5" height="5"/><rect x="8" y="4" width="5" height="5"/><rect x="15" y="4" width="5" height="5"/><line x1="1" y1="12" x2="21" y2="12"/></svg>AUTOMATION</div>
</section>
<div class="abs chat">
  <svg width="36" height="37" viewBox="0 0 36 37"><rect x="10" y="12" width="16" height="11" rx="2" fill="#fff"/><path d="M13 23l-1 4 5-4z" fill="#fff"/><circle cx="14" cy="17.5" r="1" fill="#d0021b"/><circle cx="18" cy="17.5" r="1" fill="#d0021b"/><circle cx="22" cy="17.5" r="1" fill="#d0021b"/></svg>
</div>

<section class="abs services"></section>
<h2 class="h2" style="top:384px;font-size:15px">Our Services</h2>
<p class="abs intro">In recent years, the requirements for internal logistics have become increasingly complex. In many cases, the required throughput numbers are only achievable through narrow, IT-based processes.</p>

<article class="card" style="left:158px">
  <div class="photo" role="img" aria-label="Photo: man with handheld scanner in a warehouse" style="background:linear-gradient(135deg,#b89a74,#8aa6c9)"></div>
  <div class="label" style="background:var(--blue)">KVT Development</div>
  <p>Explore the world of mobile data entry in KVT WM, IM and SD with customized mobile apps for barcode scanners, tablets or smart phones.</p>
</article>
<article class="card" style="left:277px">
  <div class="photo" role="img" aria-label="Photo: two colleagues checking a clipboard among boxes" style="background:linear-gradient(135deg,#c9a47a,#8e8f97)"></div>
  <div class="label" style="background:var(--green)">Warehouse Management</div>
  <p>Discover the comprehensive tool box for different warehouse processes incl. receiving, stag-ing, picking, packing, shipping, labeling...</p>
</article>
<article class="card" style="left:396px">
  <div class="photo" role="img" aria-label="Photo: labelled carton on a conveyor" style="background:linear-gradient(135deg,#c7a985,#bfc4ca)"></div>
  <div class="label" style="background:var(--orange)">Automation / Integration</div>
  <p>Looking for integrating print&amp;apply systems, conveyors, fix mounted scanners, sorters etc. directly into your KVT system?</p>
</article>
<article class="card" style="left:514px">
  <div class="photo" role="img" aria-label="Photo: hand holding a smartphone above a laptop keyboard" style="background:linear-gradient(135deg,#d8d2c8,#5c6f92)"></div>
  <div class="label" style="background:var(--pink)">Mobile Applications</div>
  <p>At the same time, your process-es are much faster because your employees only enter required data with the use of dialog boxes,</p>
</article>

<h2 class="h2" style="top:686px;font-size:15px">We know the various requirements of diverse industries:</h2>

<div class="industry" style="left:160px">
  <svg width="22" height="22" viewBox="0 0 22 22" fill="none" stroke="#444"><path d="M13 2v6l5 10H8l5-10"/><circle cx="6" cy="16" r="4"/><line x1="4" y1="10" x2="4" y2="12"/></svg>Chemical and<br>Pharmaceutical</div>
<div class="industry" style="left:252px">
  <svg width="30" height="22" viewBox="0 0 30 22" fill="none" stroke="#444"><path d="M1 21V12l5-3v3l5-3v12z"/><rect x="14" y="2" width="3" height="19"/><rect x="19" y="8" width="10" height="13"/><line x1="19" y1="12" x2="29" y2="12"/></svg>Mechanical and<br>Plant engineering</div>
<div class="industry" style="left:344px">
  <svg width="24" height="22" viewBox="0 0 24 22" fill="none" stroke="#444"><path d="M2 17v-6l3-6h14l3 6v6z"/><line x1="2" y1="11" x2="22" y2="11"/><circle cx="7" cy="14" r="1.5"/><circle cx="17" cy="14" r="1.5"/></svg>Automotive<br>Industrie</div>
<div class="industry" style="left:436px">
  <svg width="28" height="22" viewBox="0 0 28 22" fill="none" stroke="#444"><rect x="6" y="4" width="12" height="13"/><path d="M18 9h5l4 4v4h-9"/><circle cx="10" cy="18" r="2"/><circle cx="22" cy="18" r="2"/><line x1="0" y1="20" x2="28" y2="20"/></svg>Distribution<br>and Transportation</div>
<div class="industry" style="left:528px">
  <svg width="20" height="22" viewBox="0 0 20 22" fill="none" stroke="#444"><rect x="2" y="1" width="16" height="6"/><rect x="2" y="7" width="16" height="14"/><rect x="5" y="12" width="4" height="9"/><rect x="11" y="12" width="5" height="4"/></svg>Commerce<br>and Shopping</div>

<section class="abs news"></section>
<h2 class="h2" style="top:822px;font-size:15px">Last News</h2>
<article class="news-item" style="left:158px">
  <div class="photo" role="img" aria-label="Photo: orange robot arm in a white lab" style="background:linear-gradient(135deg,#f1f1f1,#c9cdd2)"></div>
  <h3>GHS compliant labeling</h3></article>
<article class="news-item" style="left:277px">
  <div class="photo" role="img" aria-label="Photo: automated storage hall with blue racks" style="background:linear-gradient(135deg,#8fa8cf,#3d5f9c)"></div>
  <h3>Review Options Before Investing in Warehouse Automation</h3></article>
<article class="news-item" style="left:396px">
  <div class="photo" role="img" aria-label="Photo: worker at a picking station terminal" style="background:linear-gradient(135deg,#3a5ea8,#c9c25a)"></div>
  <h3>Warehouse Automation: Who needs it?</h3></article>
<article class="news-item" style="left:515px">
  <div class="photo" role="img" aria-label="Photo: orange robot arm handling cartons" style="background:linear-gradient(135deg,#b9a78d,#d1662a)"></div>
  <h3>How Will Robots Transform The Smart Warehouse</h3></article>

<section class="abs clients"></section>
<span class="client" style="left:212px">Arvel</span>
<span class="client" style="left:264px">Corvana</span>
<span class="client" style="left:322px">Brightmoor</span>
<span class="client" style="left:384px">Halvik</span>
<span class="client" style="left:432px">Lumera</span>
<span class="client" style="left:500px">Sorenta</span>
<span class="client" style="left:548px">Senvale</span>

<div class="abs map" style="left:0;width:390px" role="img" aria-label="Street map around the USA office"></div>
<div class="abs map" style="left:391px;width:390px" role="img" aria-label="Street map around the German office"></div>
<svg class="abs" style="left:167px;top:1084px" width="8" height="10" viewBox="0 0 8 10"><path d="M4 10L1 5a3 3 0 1 1 6 0z" fill="#e05a5a"/></svg>
<svg class="abs" style="left:532px;top:1086px" width="8" height="10" viewBox="0 0 8 10"><path d="M4 10L1 5a3 3 0 1 1 6 0z" fill="#e05a5a"/></svg>

<span class="tag" style="left:171px;top:1113px">USA</span>
<div class="addr" style="left:171px;top:1133px">VANTRIX -<br>Software Solutions For Logistics, Inc.<br>240 W Harlow Rd., Suite 310<br>Marden, MI 48190</div>
<div class="addr" style="left:291px;top:1133px"><a>info@vantrix-lagerwerk.example</a><br>Tel: +1 555 014 2280<br>Fax: +1 555 014 2291</div>

<span class="tag" style="left:402px;top:1113px">GER</span>
<div class="addr" style="left:402px;top:1134px">VANTRIX GmbH -<br>Softwareloesungen der Logistik<br>Werkstrasse 14<br>61290 Almsfeld</div>
<div class="addr" style="left:509px;top:1134px"><a>info@vantrix-lagerwerk.example</a><br>Tel: +49 555 301 400<br>Fax: +49 555 301 429</div>

<footer class="abs footer">
  <span class="abs" style="left:166px;top:10px">Impring&nbsp;&nbsp;&nbsp; AGB</span>
  <span class="abs" style="left:220px;top:10px">© 2017 by VANTRIX GmbH / VANTRIX Inc.</span>
</footer>

</body>
</html>
```